Label and packaging design for a cosmetic oil brand

I would like you to design the label and inside (bottle) / outside (box) packaging of my cosmetic Argan Oil brand.

I hope you can design a high quality label and packaging that stands out from the competition, highlighting sustainability and the elegance of a cosmetic brand.

You will find in the Word document attached more details on the specifications and the text for the label. Also, you will find examples of packaging styles that I like.

Thank you.

```html
<!DOCTYPE html>
<html lang="en">
<head>
<meta charset="utf-8">
<title>Verdelune Argan Oil – Label and Box</title>
<link href="https://fonts.googleapis.com/css2?family=Noto+Sans:ital,wght@0,400;0,500;0,600;1,400;1,500&display=swap" rel="stylesheet">
<style>
  :root {
    --sage-bg: #c8d2c6;
    --label-green: #6a8758;
    --green-dark: #56714a;
    --gold: #b4934a;
    --cream: #ede7da;
    --cream-deep: #e3dccc;
    --olive-text: #6f7c46;
    --ink: #4b4a3e;
    --leaf-tone: #cfc59a;
  }
  * { box-sizing: border-box; margin: 0; padding: 0; }
  html, body { width: 746px; height: 1200px; overflow: hidden; }
  body {
    background: var(--sage-bg);
    font-family: "Noto Sans", sans-serif;
    color: var(--ink);
    position: relative;
  }

  /* ---------- Bottle label, flat ---------- */
  .bottle-label {
    position: absolute; left: 28px; top: 36px;
    width: 690px; height: 300px;
    background: var(--cream);
    box-shadow: 0 2px 8px rgba(0,0,0,.12);
  }
  .label-band {
    position: absolute; left: 0; top: 0; width: 100%; height: 116px;
    background: var(--label-green);
    border-bottom: 2px solid var(--gold);
  }
  .leaf-pattern {
    position: absolute; top: 0; height: 114px; width: 230px;
    background: linear-gradient(135deg, #6f8d5c, #5f7d50 60%, #6a8758);
  }
  .leaf-pattern.left { left: 0; }
  .leaf-pattern.right { right: 0; }
  .band-brand {
    position: absolute; left: 230px; width: 230px; top: 0; height: 114px;
    display: flex; flex-direction: column; align-items: center; justify-content: center;
  }
  .brand-dot {
    width: 34px; height: 34px; border-radius: 50%;
    border: 1.5px solid var(--gold); margin-bottom: 8px;
  }
  .brand-name {
    font-weight: 500; letter-spacing: 3px; font-size: 17px; color: var(--gold);
    text-transform: uppercase;
  }
  .brand-tagline { font-size: 8px; color: #e9dfc0; margin-top: 2px; }

  .label-body {
    position: absolute; left: 0; top: 118px; width: 100%; height: 182px;
    display: grid; grid-template-columns: 230px 230px 230px;
  }
  .label-col { padding: 16px 18px; font-size: 8.5px; line-height: 1.5; }
  .label-col.side { font-style: italic; color: var(--olive-text); text-align: justify; }
  .label-col.side p + p { margin-top: 8px; }
  .label-col.side b { font-weight: 600; }
  .label-col.side.en { font-style: normal; color: var(--ink); }
  .recycle-marks { display: flex; gap: 5px; justify-content: flex-end; margin-top: 10px; }
  .recycle-marks span { width: 11px; height: 11px; border-radius: 50%; background: var(--ink); }

  .front-copy { text-align: center; color: var(--olive-text); }
  .front-copy .line-a { font-size: 11px; }
  .front-copy .line-b { font-size: 14px; }
  .front-copy .line-c { font-size: 9.5px; font-style: italic; color: var(--ink); font-weight: 500; margin-top: 4px; line-height: 1.3; }
  .front-copy .line-d { font-size: 11px; margin-top: 14px; }
  .front-copy .line-e { font-size: 9.5px; font-style: italic; color: var(--ink); line-height: 1.3; margin-top: 2px; }
  .front-copy .size { font-size: 9.5px; margin-top: 14px; }

  /* ---------- Outer box panels ---------- */
  .box-front, .box-back {
    position: absolute; top: 372px; width: 336px; height: 508px;
    background: var(--cream);
    box-shadow: 0 2px 8px rgba(0,0,0,.12);
  }
  .box-front { left: 28px; }
  .box-back { left: 382px; }

  .box-front .mark {
    margin: 70px auto 0; width: 58px; height: 58px; border-radius: 50%;
    border: 1.5px solid var(--gold);
  }
  .box-front .brand-name { display: block; text-align: center; font-size: 22px; margin-top: 20px; }
  .box-front .brand-tagline { text-align: center; color: var(--gold); font-size: 10px; margin-top: 2px; }
  .box-copy { text-align: center; color: var(--olive-text); margin-top: 44px; }
  .box-copy .line-a { font-size: 15px; }
  .box-copy .line-b { font-size: 19px; }
  .box-copy .line-c { font-size: 13px; font-style: italic; font-weight: 500; color: var(--ink); margin-top: 6px; line-height: 1.35; }
  .box-copy .rule { width: 70px; height: 1.5px; background: var(--olive-text); margin: 26px auto; }
  .box-copy .line-d { font-size: 15px; }
  .box-copy .line-e { font-size: 13px; font-style: italic; color: var(--ink); margin-top: 4px; line-height: 1.35; }
  .box-copy .size { font-size: 14px; margin-top: 30px; font-weight: 500; }

  .box-back { padding: 26px 22px; font-size: 8.5px; line-height: 1.5; }
  .back-columns { display: grid; grid-template-columns: 1fr 1fr; gap: 14px; }
  .back-columns p + p { margin-top: 8px; }
  .back-columns b { font-weight: 600; }
  .benefits {
    margin-top: 20px; border: 1px solid var(--ink); padding: 8px 10px;
    font-size: 7.5px; line-height: 1.5;
  }
  .benefits h3 { text-align: center; font-size: 8.5px; font-weight: 600; letter-spacing: 1px; margin-bottom: 4px; }
  .back-footer { margin-top: 20px; font-size: 7.5px; line-height: 1.5; }
  .back-footer p + p { margin-top: 6px; }
  .cert-badges { display: flex; gap: 6px; justify-content: flex-end; margin-top: 14px; }
  .cert-badges span { width: 14px; height: 14px; border-radius: 50%; border: 1px solid var(--ink); }

  /* ---------- Box lid interior ---------- */
  .lid-inside {
    position: absolute; left: 28px; top: 916px; width: 690px; height: 248px;
    background: var(--cream-deep);
    box-shadow: 0 2px 8px rgba(0,0,0,.12);
  }
  .lid-pattern {
    position: absolute; inset: 0;
    background: radial-gradient(ellipse at center, var(--cream-deep) 30%, var(--leaf-tone) 130%);
  }
  .lid-center {
    position: absolute; left: 250px; top: 82px; width: 200px; height: 84px;
    display: flex; align-items: center; gap: 14px;
  }
  .sketch-spot {
    width: 56px; height: 56px; flex: none; background: linear-gradient(160deg, #d6c38a, #c4ab6a);
    border-radius: 6px; opacity: .8;
  }
  .lid-text { font-size: 8.5px; color: var(--gold); line-height: 1.5; }
  .lid-socials { display: flex; gap: 6px; margin-top: 6px; }
  .lid-socials span { width: 10px; height: 10px; border-radius: 50%; background: var(--gold); }
</style>
</head>
<body>

  <section class="bottle-label" aria-label="Bottle label, laid flat">
    <div class="label-band">
      <div class="leaf-pattern left" role="img" aria-label="Line drawing of argan leaves and nuts in soft tone on green"></div>
      <div class="band-brand">
        <span class="brand-dot"></span>
        <span class="brand-name">Verdelune</span>
        <span class="brand-tagline">Pure daily care, grown with respect for the land</span>
      </div>
      <div class="leaf-pattern right" role="img" aria-label="Line drawing of argan leaves and nuts in soft tone on green"></div>
    </div>
    <div class="label-body">
      <div class="label-col side">
        <p><b>Ingrédients:</b> Un seul ! Huile d'Argania Spinosa (Argan) 100% pure, pressée à froid et non parfumée, une riche source d'acides gras, d'antioxydants et de vitamine E.</p>
        <p><b>Mise en garde:</b> Pour usage externe uniquement, tenir hors des yeux. En cas de sensibilité cutanée, cesser l'utilisation.</p>
        <div class="recycle-marks"><span></span><span></span></div>
      </div>
      <div class="label-col front-copy">
        <div class="line-a">100% Pure Cosmetic</div>
        <div class="line-b">Argan Oil of Morocco</div>
        <div class="line-c">Huile d'Argan cosmétique<br>du Maroc 100% pure</div>
        <div class="line-d">Natural Hair and Skin Care</div>
        <div class="line-e">Soins naturels<br>de la peau et des cheveux</div>
        <div class="size">1 oz | 30 ml</div>
      </div>
      <div class="label-col side en">
        <p>Ingredients: Only one ! 100% pure, cold-pressed and unscented Argania Spinosa (Argan) kernel Oil, a rich source of fatty acids, antioxidants, and vitamin E.</p>
        <p>Caution: For external use only, keep out of the eyes. If skin sensitivity occurs, discontinue use.</p>
      </div>
    </div>
  </section>

  <section class="box-front" aria-label="Box front panel">
    <div class="mark"></div>
    <span class="brand-name">Verdelune</span>
    <div class="brand-tagline">Pure daily care, grown with respect for the land</div>
    <div class="box-copy">
      <div class="line-a">100% Pure Cosmetic</div>
      <div class="line-b">Argan Oil of Morocco</div>
      <div class="line-c">Huile d'Argan cosmétique<br>du Maroc 100% pure</div>
      <div class="rule"></div>
      <div class="line-d">Natural Hair and Skin Care</div>
      <div class="line-e">Soins naturels<br>de la peau et des cheveux</div>
      <div class="size">1 oz | 30 ml</div>
    </div>
  </section>

  <section class="box-back" aria-label="Box back panel">
    <div class="back-columns">
      <div>
        <p><b>Ingredients:</b> Only one ! 100% pure, cold-pressed and unscented Argania Spinosa (Argan) kernel Oil, a rich source of fatty acids, antioxidants, and vitamin E.</p>
        <p><b>Caution:</b> For external use only, keep out of the eyes. If skin sensitivity occurs, discontinue use.</p>
      </div>
      <div>
        <p><b>How to use:</b> Apply to your hair and scalp to nourish, condition and style. Apply to your face, skin and nails to hydrate, moisturize and condition. Use daily for better results. You can also use it as a massage or bath oil.</p>
      </div>
    </div>
    <div class="benefits">
      <h3>BENEFITS</h3>
      <p>Argan Oil is considered one of nature's richest sources of essential fatty acids, antioxidants, and vitamin E. Its unique composition grants it amazing conditioning and nourishing properties that naturally promote healthy, radiant, youthful skin and hair. Besides, Verdelune Argan Oil supports Fair-Trade certified women-led cooperatives in underdeveloped rural areas, contributing to their local economy and ensuring the good exploitation of the protected Argan tree. In short, it will allow you to take care of your health and beauty, while caring for the land !</p>
    </div>
    <div class="back-footer">
      <p>Visit <b>verdelune.com</b> for more information and details on Verdelune Argan Oil, its benefits and how to use it.</p>
      <p>Imported from Morocco | Bottled and Distributed by Verdelune<br>Lakeford, ON, Canada</p>
    </div>
    <div class="cert-badges"><span></span><span></span><span></span><span></span><span></span><span></span></div>
  </section>

  <section class="lid-inside" aria-label="Inside of box lid">
    <div class="lid-pattern" role="img" aria-label="Gold line drawing of argan branches, leaves and nuts scattered across cream"></div>
    <div class="lid-center">
      <div class="sketch-spot" role="img" aria-label="Gold sketch of an argan oil bottle with fruit"></div>
      <div>
        <div class="lid-text">verdelune.com<br>Pure daily care, grown<br>with respect for the land</div>
        <div class="lid-socials"><span></span><span></span><span></span></div>
      </div>
    </div>
  </section>

</body>
</html>
```